Paperback Book Cover Design

I need a professional cover designed for my new book. You must use the design template enclosed. The title of the book is “Open Your Digital Purse Now!” The graphic used on the book cover should of course relate to making money online through various skills such as writing, graphic design, online marketing, photography, trading, Tradlo etc. The graphic(s) used must demonstrate to the reader that the book gives various ways to make money online.

At the top of the book you must include the sub heading “Earn From Home Collection”. The main title of the book is “Open Your Digital Purse Now!”, which of course should be highly prominent on the front cover. The front cover must also include the author name, Gerald Whitcombe.

I have no preference to colours used so do be creative to create an eye catching cover design.

The spine of the book should include the main title and the author name. Feel free to use an image or images for the rear of the book and just add dummy text.

The winning designer must supply a layered psd file complete with all fonts and elements used.

Industry/Entity Type

Graphic Design

Requirements
Must have
• The winning designer must supply a layered psd file complete with all fonts and elements used.

```html
<!DOCTYPE html>
<html lang="en">
<head>
<meta charset="utf-8">
<title>Open Your Digital Purse Now! – Paperback Cover Spread</title>
<link rel="stylesheet" href="https://fonts.googleapis.com/css2?family=Anton&family=Arimo:wght@700&family=Cinzel:wght@400;600&family=Permanent+Marker&family=Open+Sans:wght@400&display=swap">
<style>
  :root {
    --page-white: #ffffff;
    --cover-cream: #ecebe3;
    --spine-cream: #e6e5dc;
    --copy-panel: #c9c9c9;
    --ink: #111111;
    --copy-ink: #2e2e2e;
    --green-light: #9cff3c;
    --green-mid: #3ee01a;
    --green-deep: #12a50a;
    --accent-red: #e8141b;
    --orange-light: #ffa23a;
    --orange-deep: #c35a05;
    --shadow-brown: #3a1d08;
    --laptop-grey: #8d9190;
    --cash-green: #b9c7a6;
  }
  * { box-sizing: border-box; margin: 0; padding: 0; }
  html, body { width: 1200px; height: 1000px; overflow: hidden; background: var(--page-white); }
  .canvas { position: relative; width: 1200px; height: 1000px; }

  .back-cover { position: absolute; left: 33px; top: 90px; width: 527px; height: 790px; background: var(--page-white); }
  .spine { position: absolute; left: 560px; top: 90px; width: 86px; height: 790px; background: var(--spine-cream); overflow: hidden; }
  .front-cover { position: absolute; left: 646px; top: 90px; width: 526px; height: 790px; background: var(--cover-cream); overflow: hidden; }

  .series-label { font-family: "Arimo", Arial, sans-serif; font-weight: 700; color: var(--ink); white-space: nowrap; }
  .title-line {
    font-family: "Anton", "Oswald", sans-serif;
    text-transform: uppercase;
    display: block;
    white-space: nowrap;
    background: linear-gradient(180deg, var(--green-light) 0%, var(--green-mid) 55%, var(--green-deep) 100%);
    -webkit-background-clip: text;
    background-clip: text;
    color: transparent;
  }
  .title-accent { font-family: "Permanent Marker", cursive; color: var(--accent-red); white-space: nowrap; position: absolute; transform: rotate(-9deg); transform-origin: left bottom; }

  /* Back cover */
  .back-cover .series-label { position: absolute; left: 31px; top: 30px; font-size: 17px; }
  .back-title { position: absolute; left: 26px; top: 50px; }
  .back-title .title-line { font-size: 56px; line-height: 47px; letter-spacing: -0.5px; }
  .back-cover .title-accent { left: 160px; top: 224px; font-size: 40px; }

  .blurb-panel { position: absolute; left: 265px; top: 0; width: 262px; height: 455px; background: var(--copy-panel); padding: 7px 8px 0 8px; }
  .blurb-panel p { font-family: "Open Sans", Arial, sans-serif; font-size: 6.6px; line-height: 8.6px; color: var(--copy-ink); text-align: justify; margin-bottom: 8px; }

  .back-photo { position: absolute; left: 16px; top: 515px; width: 440px; height: 245px; border-radius: 6px;
    background: radial-gradient(ellipse at 62% 40%, var(--cash-green) 0%, #d9ddd1 45%, rgba(255,255,255,0) 72%), linear-gradient(150deg, #3b3d3f 0%, var(--laptop-grey) 40%, #e9ebe7 75%); }

  /* Spine */
  .spine-text { position: absolute; left: 6px; top: 10px; height: 680px; writing-mode: vertical-rl; display: flex; flex-direction: column; align-items: flex-start; gap: 2px; }
  .spine .series-label { font-size: 19px; line-height: 24px; }
  .spine .title-line { font-size: 46px; line-height: 48px; letter-spacing: 0.5px;
    background: linear-gradient(90deg, var(--green-light), var(--green-mid) 55%, var(--green-deep)); -webkit-background-clip: text; background-clip: text; }
  .spine-author { position: absolute; left: 0; width: 86px; top: 706px; text-align: center; font-family: "Cinzel", serif; font-size: 13px; line-height: 16px; color: var(--ink); }

  /* Front cover */
  .front-art { position: absolute; left: 0; top: 160px; width: 526px; height: 460px;
    background: linear-gradient(135deg, rgba(255,162,58,0) 0%, var(--orange-light) 22%, var(--orange-deep) 60%, var(--shadow-brown) 82%, rgba(58,29,8,0) 100%); opacity: 0.9; }
  .front-cover .series-label { position: absolute; left: 36px; top: 26px; font-size: 29px; }
  .front-title { position: absolute; left: 30px; top: 56px; }
  .front-title .title-line { font-size: 136px; line-height: 122px; letter-spacing: -1px; }
  .front-cover .title-accent { left: 200px; top: 488px; font-size: 96px; }
  .front-author { position: absolute; left: 0; width: 526px; top: 738px; text-align: center; font-family: "Cinzel", serif; font-size: 29px; color: var(--ink); letter-spacing: 0.5px; }
</style>
</head>
<body>
<main class="canvas">

  <section class="back-cover">
    <div class="series-label">Earn From Home Collection:</div>
    <h2 class="back-title">
      <span class="title-line">Open</span>
      <span class="title-line">Your</span>
      <span class="title-line">Digital</span>
      <span class="title-line">Purse</span>
    </h2>
    <span class="title-accent">Now!</span>

    <div class="blurb-panel">
      <p>Working from home begins with one clear choice and a plan you can follow each day. Pick a skill you enjoy, set small weekly goals and track every result. Writing, design, photos and trading all reward steady practice, honest service and patient growth over many months of focused effort.</p>
      <p>Freelance writing suits anyone who reads widely and meets deadlines. Start with short articles, build a small portfolio and ask each client for feedback. Rates rise as your samples improve, so keep learning new formats such as guides, product pages, newsletters and clear emails for small firms.</p>
      <p>Graphic design work ranges from logos and flyers to full book covers. Learn the basics of type, colour and layout, then enter open contests to practise. Each finished job adds a piece to your gallery and brings new buyers who return with larger projects later.</p>
      <p>Online marketing helps small shops reach people who want their goods. Study search, email lists and social posts, then test ideas with a tiny budget first. Measure clicks and sales, drop what fails and repeat what works until the numbers grow.</p>
      <p>Photography pays through stock sites, local events and product shoots. Keep your gear simple, learn good light and edit with care. Upload often, tag each image well and let a growing library earn small sums every single month.</p>
      <p>Trading goods on Tradlo starts with items already in your home. Clean them, take sharp photos and write honest notes. Ship quickly, answer questions the same day and your ratings will climb, bringing more buyers to each new listing you post.</p>
      <p>Money earned online still needs careful handling. Keep simple records, set aside tax each month and save a share of every payment. Small habits protect your income and give you room to try the next idea without fear.</p>
      <p>This book gathers proven paths in one place, with plain steps, real examples and checklists you can use today. Read a chapter, choose one method and begin. Your digital purse opens the moment you take the first small action.</p>
    </div>

    <div class="back-photo" role="img" aria-label="Photo of an open laptop with dollar banknotes flying out of the screen"></div>
  </section>

  <section class="spine">
    <div class="spine-text">
      <span class="series-label">Earn From Home Collection:</span>
      <span class="title-line">Open Your Digital Purse Now</span>
    </div>
    <div class="spine-author">BY:<br>GERALD<br>WHITCOMBE</div>
  </section>

  <section class="front-cover">
    <div class="front-art" role="img" aria-label="Illustration of large orange 3D boxes breaking apart behind the title"></div>
    <div class="series-label">Earn From Home Collection:</div>
    <h1 class="front-title">
      <span class="title-line">Open</span>
      <span class="title-line">Your</span>
      <span class="title-line">Digital</span>
      <span class="title-line">Purse</span>
    </h1>
    <span class="title-accent">Now!</span>
    <div class="front-author">BY: GERALD WHITCOMBE</div>
  </section>

</main>
</body>
</html>
```